psd/html for a e wallet payment website designed

hi
i am in need of a psd / html for a whole website designed
the site is a e wallet /payment system i can i will provide a link to what type of style i am looking for but i can not stress this enough i do not want anyone replicating the website i am just providing the links to show you what kind of function and the content that is involved also, i have a srs with detailed pages you can read and refer to if need be
thanks of viewing
Vantoleaf.com
Brisklune.com
marblequivercoin.com
Qrdelivane.com

```html
<!DOCTYPE html>
<html lang="en">
<head>
<meta charset="utf-8">
<title>Corvane Pay</title>
<link href="https://fonts.googleapis.com/css2?family=Open+Sans:ital,wght@0,300;0,400;0,600;1,400&display=swap" rel="stylesheet">
<style>
:root{
  --navy:#1f3d63;
  --navy-dark:#15304f;
  --navy-light:#2f5a88;
  --orange:#f08a1c;
  --text:#555b63;
  --muted:#9aa0a6;
  --line:#dcdfe3;
  --band:#eef0f2;
  --white:#ffffff;
  --footer-top:#2f5985;
  --footer-bot:#1a3558;
}
*{margin:0;padding:0;box-sizing:border-box}
html,body{width:739px;height:1200px;overflow:hidden;background:var(--white)}
body{position:relative;font-family:"Open Sans",Arial,sans-serif;color:var(--text)}
.abs{position:absolute}
/* header */
.brand{left:47px;top:18px;display:flex;align-items:center;gap:6px}
.brand-name{font-size:26px;font-weight:400;color:var(--navy);letter-spacing:-.3px}
.brand-square{width:14px;height:14px;background:var(--orange)}
.btn{top:10px;height:17px;width:48px;border-radius:3px;font-size:7px;font-weight:600;color:var(--white);text-align:center;line-height:17px;text-transform:uppercase}
.btn-signup{left:588px;background:var(--navy)}
.btn-login{left:639px;background:var(--orange)}
.social{left:611px;top:41px;display:flex;gap:6px}
.social span{width:14px;height:14px;background:var(--navy-light);border-radius:2px}
/* nav */
.nav{left:47px;top:64px;width:645px;height:31px;background:linear-gradient(var(--navy-light),var(--navy-dark));border-radius:3px 3px 0 0;display:flex;overflow:hidden}
.nav a{flex:none;color:var(--white);text-decoration:none;font-size:10.5px;line-height:31px;text-align:center;white-space:nowrap;border-right:1px solid rgba(0,0,0,.25)}
.nav a:last-child{border-right:0}
.nav .w-home{width:61px}
.nav .w-about{width:76px}
.nav .w-exchange{width:75px}
.nav .w-fees{width:76px}
.nav .w-merchants{width:80px}
.nav .w-developers{width:87px}
.nav .w-help{width:52px}
.nav .w-service{width:64px}
.nav .w-support{width:74px}
/* hero */
.hero-band{left:0;top:95px;width:739px;height:257px;background:linear-gradient(var(--band),#f8f9fa)}
.hero{left:47px;top:95px;width:645px;height:238px;background:var(--white);box-shadow:0 1px 3px rgba(0,0,0,.12)}
.hero-kicker{left:84px;top:148px;font-size:18.5px;color:var(--orange);white-space:nowrap}
.hero-title{left:84px;top:173px;font-size:26px;color:var(--navy);white-space:nowrap}
.hero-text{left:87px;top:211px;width:238px;font-size:8px;line-height:12.5px;color:var(--text)}
.dots{left:87px;top:256px;display:flex;gap:3px}
.dots span{width:7px;height:7px;border-radius:50%;background:#9fb1c6}
.dots span:first-child{background:var(--navy)}
.hero-photo{left:440px;top:98px;width:165px;height:235px;background:linear-gradient(180deg,#d8e0ec,#a9c3e6);border-radius:80px 80px 0 0}
/* intro */
.intro-title{left:0;top:376px;width:739px;text-align:center;font-size:22px;color:var(--navy)}
.intro-text{left:85px;top:407px;width:570px;text-align:center;font-size:7.5px;line-height:13.5px}
/* features */
.card{width:207px;height:86px;border:1px solid var(--line);border-radius:3px;background:linear-gradient(#fff 60%,#f1f2f4)}
.card-icon{position:absolute;left:10px;top:20px;width:40px;height:40px;border-radius:50%}
.card h3{position:absolute;left:54px;top:12px;font-size:14px;font-weight:400;color:var(--orange);white-space:nowrap}
.card p{position:absolute;left:55px;top:33px;width:145px;font-size:7px;line-height:11.5px;color:var(--muted)}
/* welcome & news */
.sec-title{font-size:17px;font-weight:400;white-space:nowrap}
.welcome-title{left:48px;top:687px;color:var(--orange)}
.welcome-img{left:47px;top:720px;width:87px;height:93px;background:linear-gradient(135deg,#3c4a5c,#7fa6cf 55%,#d8c79a)}
.welcome-text{left:142px;top:716px;width:298px;font-size:7.6px;line-height:14px}
.welcome-text p+p{margin-top:5px}
.news-title{left:470px;top:687px;color:var(--navy)}
.news{left:472px;width:215px}
.news h4{font-size:9px;font-weight:600;color:var(--navy)}
.news p{font-size:7px;line-height:11px;margin-top:3px}
.divider{left:48px;top:854px;width:628px;height:1px;background:var(--line)}
/* testimonials */
.testi-title{left:0;top:879px;width:739px;text-align:center;font-size:17px;color:#3b4350;font-weight:300}
.avatar{width:56px;height:56px;border-radius:50%;border:3px solid #fff;box-shadow:0 0 0 1px var(--line);background:linear-gradient(#e2c4a8,#a9856a)}
.quote{width:138px;font-size:7.3px;font-style:italic;line-height:12.5px}
.author{font-size:8.5px;font-weight:600;color:var(--orange);font-style:normal;margin-top:7px}
/* footer */
.footer{left:0;top:1011px;width:739px;height:189px;background:linear-gradient(var(--footer-top),var(--footer-bot))}
.fcol{top:1037px;color:var(--white)}
.fcol h5{font-size:11.5px;font-weight:400;margin-bottom:4px}
.fcol li{list-style:none;font-size:8px;line-height:15.2px;color:#d9e2ec}
.fsep{top:1036px;width:1px;height:102px;background:rgba(255,255,255,.15)}
.footer-bar{left:5px;top:1160px;width:734px;height:40px;background:rgba(0,0,0,.12);border-top:1px solid rgba(255,255,255,.06)}
.copy{left:55px;top:1173px;font-size:7.5px;color:#8fa3bb}
</style>
</head>
<body>
<header>
  <div class="abs brand"><span class="brand-name">Corvane Pay</span><span class="brand-square"></span></div>
  <div class="abs btn btn-signup">Sign up</div>
  <div class="abs btn btn-login">Login</div>
  <div class="abs social" aria-label="Social links"><span></span><span></span><span></span><span></span></div>
  <nav class="abs nav">
    <a class="w-home" href="#">Home</a><a class="w-about" href="#">About Us</a><a class="w-exchange" href="#">Exchange</a><a class="w-fees" href="#">Pay Fees</a><a class="w-merchants" href="#">Merchants</a><a class="w-developers" href="#">Developers</a><a class="w-help" href="#">Help</a><a class="w-service" href="#">Service</a><a class="w-support" href="#">Support</a>
  </nav>
</header>

<section>
  <div class="abs hero-band"></div>
  <div class="abs hero"></div>
  <div class="abs hero-kicker">Maecenas at justo placerat</div>
  <h1 class="abs hero-title" style="font-weight:400">Quisque dignissim congue</h1>
  <p class="abs hero-text">Lorem ipsum dolor sit amet, consectetuer adipiscing elit. Nam cursus. Morbi ut mi. Nullam enim leo, egestas id, condimentum at, laoreet mattis, massa.</p>
  <div class="abs dots"><span></span><span></span><span></span><span></span></div>
  <div class="abs hero-photo" role="img" aria-label="Photo of a smiling businesswoman with glasses, arms crossed"></div>
</section>

<section>
  <h2 class="abs intro-title" style="font-weight:400">Donec dictum lectus non odio rasa</h2>
  <p class="abs intro-text">Quisque dignissim congue leo.auris vel lacus vitae felis vestibulum volutpat. Etiam est nunc, venenatis in, tristique eu, imperdiet ac, nisl. Cum sociis natoque penatibus et magnis dis parturient montes, nascetur ridiculus mus. In iaculis facilisis massa. Etiam eu urna. Sed porta. Suspendisse quam leo, molestie sed, luctus quis, feugiat in, pede. Fusce tellus. Sed metus augue, convallis et</p>

  <div class="abs card" style="left:47px;top:463px"><div class="card-icon" role="img" aria-label="Globe illustration" style="background:radial-gradient(#7ec3ea,#e39a2e)"></div><h3>Global Money Tranfer</h3><p>Conec convallis pede venenatis nibh. Duis quam. Nam eget lacus. Aliquam erat volutpat. Quisque dignissim congue</p></div>
  <div class="abs card" style="left:262px;top:463px"><div class="card-icon" role="img" aria-label="Stack of banknotes illustration" style="background:linear-gradient(#c9d8b0,#6f8f4f);border-radius:4px"></div><h3>Payrolls &amp; Accounts</h3><p>Conec convallis pede venenatis nibh. Duis quam. Nam eget lacus. Aliquam erat volutpat. Quisque dignissim congue</p></div>
  <div class="abs card" style="left:477px;top:463px"><div class="card-icon" role="img" aria-label="Invoice document illustration" style="background:linear-gradient(#f3f5f8,#9bb4d3);border-radius:4px"></div><h3>Invoice &amp; Accounting</h3><p>Conec convallis pede venenatis nibh. Duis quam. Nam eget lacus. Aliquam erat volutpat. Quisque dignissim congue</p></div>
  <div class="abs card" style="left:47px;top:561px"><div class="card-icon" role="img" aria-label="Stacks of gold coins illustration" style="background:linear-gradient(#f5d27a,#c98a1a);border-radius:4px"></div><h3>Easy Withdraw</h3><p>Conec convallis pede venenatis nibh. Duis quam. Nam eget lacus. Aliquam erat volutpat. Quisque dignissim congue</p></div>
  <div class="abs card" style="left:262px;top:561px"><div class="card-icon" role="img" aria-label="Support agent with headset illustration" style="background:linear-gradient(#f0c9a6,#c9cdd3)"></div><h3>24/7 Support</h3><p>Conec convallis pede venenatis nibh. Duis quam. Nam eget lacus. Aliquam erat volutpat. Quisque dignissim congue</p></div>
  <div class="abs card" style="left:477px;top:561px"><div class="card-icon" role="img" aria-label="Padlock illustration" style="background:linear-gradient(#e6e8eb,#8d9299);border-radius:4px"></div><h3>Safe environment</h3><p>Conec convallis pede venenatis nibh. Duis quam. Nam eget lacus. Aliquam erat volutpat. Quisque dignissim congue</p></div>
</section>

<section>
  <h2 class="abs sec-title welcome-title">Welcome to Our Website Mainpage</h2>
  <div class="abs welcome-img" role="img" aria-label="Photo of bank cards and a smartphone on a keyboard"></div>
  <div class="abs welcome-text">
    <p>Maecenas at justo id velit placerat molestie. Donec dictum lectus non odio. Cras a ante vitae enim iaculis aliquam. Mauris nunc quam, venenatis nec, euismod sit amet, egestas placerat, est. Pellentesque habitant morbi tristique senectus et netus et malesuada fames ac turpis egestas</p>
    <p>Cras id elit. Integer quis urna. Ut ante enim, dapibus malesuada, fringilla eu, condimentum quis, tellus. Aenean porttitor eros vel dolor. Donec convallis pede venenatis nibh. Duis quam. Nam eget lacus. Aliquam erat volutpat</p>
  </div>
  <h2 class="abs sec-title news-title">Recent News &amp; Blog</h2>
  <div class="abs news" style="top:718px"><h4>Conec convallis pede venenatis</h4><p>Etiam est nunc, venenatis in, tristique eu, imperdiet nisl. Cum sociis natoque penatibus et magnis dis parturient montes,</p></div>
  <div class="abs news" style="top:768px"><h4>Nulla sit amet diam</h4><p>Duis non nunc. Nulla rhoncus dictum metus. Curabitur tristique mi condimentum orci. Phasellus pellentesque aliquam enim</p></div>
  <div class="abs divider"></div>
</section>

<section>
  <h2 class="abs testi-title">What Our Customers Say</h2>
  <div class="abs avatar" style="left:58px;top:910px" role="img" aria-label="Customer portrait"></div>
  <div class="abs quote" style="left:122px;top:911px">Suspendisse quam leo, molestie sed, luctus quis, feugiat in, pede. Fusce tellus. Sed metus augue, convallis et, vehicula ut, pulvinar eu, ante. Integer orci tellus, tristique vitae<div class="author">By Author Name</div></div>
  <div class="abs avatar" style="left:279px;top:916px" role="img" aria-label="Customer portrait"></div>
  <div class="abs quote" style="left:344px;top:917px">Morbi eget arcu. Morbi porta, libero id ullamcorper nonummy, nibh ligula pulvinar metus, eget consv et scelerisque mi tortor at ipsum<div class="author">By Author Name</div></div>
  <div class="abs avatar" style="left:494px;top:914px" role="img" aria-label="Customer portrait"></div>
  <div class="abs quote" style="left:558px;top:913px;width:140px">In massa libero, interdum nec, interdum vel, blandit sed, nulla. In ullamcorper, est eget tempor cursus, neque mi consectetuer mi, a ultricies massa est sed nisl.<div class="author">By Author Name</div></div>
</section>

<footer>
  <div class="abs footer"></div>
  <div class="abs fcol" style="left:63px"><h5>Company</h5><ul><li>About Us</li><li>Customers</li><li>Locations</li><li>Newsletters</li><li>Contact Us</li></ul></div>
  <div class="abs fsep" style="left:157px"></div>
  <div class="abs fcol" style="left:181px"><h5>Services</h5><ul><li>Web Design</li><li>CMS</li><li>Online Marketing</li><li>Email Marketing</li><li>Analysis</li></ul></div>
  <div class="abs fsep" style="left:279px"></div>
  <div class="abs fcol" style="left:298px"><h5>Support</h5><ul><li>Search Engine</li><li>Multilingual</li><li>Social Media</li></ul></div>
  <div class="abs fsep" style="left:378px"></div>
  <div class="abs fcol" style="left:402px"><h5>Sublinks</h5><ul><li>Donec scelerisque</li><li>Leo ac risus</li><li>Praesent sit amet</li><li>Est dictum dolor</li><li>Dictum porttitor</li></ul></div>
  <div class="abs fsep" style="left:497px"></div>
  <div class="abs fcol" style="left:514px"><h5>Sublinks</h5><ul><li>Etiam eu urna</li><li>Sed porta</li><li>Suspendisse quam</li></ul></div>
  <div class="abs footer-bar"></div>
  <div class="abs copy">© 2013 Company Name. All right reserved. Term of Use</div>
</footer>
</body>
</html>
```